8' X 8" convention booth design

I am requesting a design for a convention booth. This design must be created in Adobe Illustrator.
I sell insurance programs to the members of associations. My prospects that will see this booth are association professionals looking to select a provider of insurance benefits for their memberships. I would like my prospects to look at my booth, see our logo, understand what we do, and then show some icons highlighting the insurance products that we have available. Please feel free to add any pictures or anything you might find to make the booth more appealing, but are not necessary. I have attached a photo of a sample of the booth construction below for your review.
The booth is 8’ X 8’ in the front and will have two 1’ side panels on each side. The dimensions of the front graphics are 87.75” W X 87.75” H. Each of the two side panel is 12 W X 87.75” H. The total width of the design is 111.75”. The graphic should be designed to include the 12’ wrap around on each side.
I have attached two of our logos below. The attached Zelqa logo with the words "Affinity and Association Services" is the logo for the front of the booth. The plain Zelqa logo is for the top of the side panels.
For side panels, please put the Zelqa logo (with only the Zelqa letters) at the top and the words "Association Insurance" underneath the Zelqa logo. The Association Insurance letters should be vertical.
For the front of the booth, I would like to have the Zelqa logo somewhere prominent in your design. I do not want it too big, but would like people to notice my company logo and description line. Also on the front of the booth, please include the following information that describes my company:
Full Portfolio of Insurance Products
Brokerage with A-Rated insurance companies
Full-Service Administrator
State-of-the-Art Technologies
Multi-Channel Marketing
The header for this section of five bullets above can be Member Insurance Program Management.
Lastly, I have attached 14 other icons that represent the insurance products I am offering. Please place them in a grid, or some other creative way, and include the word I have used to name each icon below each icon. For example, please type the word Life under the Life icon in the design. If you are looking for a header for this section, it can be Insurance Products Thank you very much for your interest.
Association Executive Directors looking to offer valuable member benefits to their association membership.

```html
<!DOCTYPE html>
<html lang="en">
<head>
<meta charset="utf-8">
<title>Zelqa Association Insurance Booth</title>
<link href="https://fonts.googleapis.com/css2?family=Poppins:ital,wght@0,400;0,500;0,600;0,700;1,400&display=swap" rel="stylesheet">
<style>
:root{
  --green:#9fa617;
  --dark:#2f2f2f;
  --ink:#2b2b2b;
  --grey-text:#444;
  --paper:#ffffff;
  --paper-soft:#f3f3f3;
  --stage:#e6e6e6;
}
*{box-sizing:border-box;margin:0;padding:0}
html,body{width:1200px;height:1003px;overflow:hidden}
body{background:var(--stage);font-family:"Poppins",sans-serif;position:relative}

.side-panel{position:absolute;top:72px;width:114px;height:833px;background:var(--paper)}
.side-panel--left{left:62px}
.side-panel--right{left:1024px}
.side-panel__brand{height:160px;display:flex;align-items:center;justify-content:center;
  font-weight:700;font-size:30px;color:var(--green)}
.side-panel__band{height:673px;display:flex;flex-direction:column;align-items:center;
  padding-top:36px;color:#fff;font-weight:700;font-size:24px;line-height:29.3px}
.side-panel--left .side-panel__band{background:var(--green)}
.side-panel--right .side-panel__band{background:var(--dark)}
.side-panel__gap{height:29px}

.front{position:absolute;left:184px;top:72px;width:835px;height:833px;overflow:hidden;
  background:linear-gradient(115deg,var(--paper) 0 38%,var(--paper-soft) 38% 100%)}
.front__header{position:absolute;left:0;top:42px;width:100%;height:78px}
.front__brand{position:absolute;left:130px;top:8px;font-weight:700;font-size:50px;color:var(--green);line-height:62px}
.front__divider{position:absolute;left:290px;top:14px}
.front__tagline{position:absolute;left:326px;top:25px;font-style:italic;font-size:20px;letter-spacing:2.4px;color:var(--grey-text);white-space:nowrap}

.program{position:absolute;left:0;top:162px;width:100%;height:214px}
.program svg{position:absolute;inset:0}
.program__title{position:absolute;left:68px;top:32px;color:#fff;font-weight:700;font-size:34px;line-height:40px;letter-spacing:.5px}
.program__list{list-style:none;position:absolute;top:0;left:0;color:#fff;font-size:19px}
.program__list li{position:absolute;white-space:nowrap;display:flex;align-items:center;gap:8px}
.program__list li::before{content:"»";color:var(--green);font-weight:700;font-size:22px;line-height:1}

.products__title{position:absolute;left:0;width:100%;top:402px;text-align:center;font-weight:700;font-size:28px;color:var(--ink);letter-spacing:.5px}
.product{position:absolute;width:100px;text-align:center}
.product__icon{display:block;margin:0 auto;width:80px;height:80px;border-radius:50%;
  background:radial-gradient(circle at 50% 50%,#cfe4f7 0 34%,#fff 35%);
  box-shadow:-10px 8px 14px rgba(0,0,0,.18)}
.product__label{display:block;margin-top:14px;font-weight:600;font-size:14px;line-height:17px;color:var(--ink)}

.contact{position:absolute;left:240px;top:760px;width:354px;height:27px;border-radius:14px;overflow:hidden;display:flex;font-weight:700;font-size:14px}
.contact__phone{background:var(--green);color:#fff;width:186px;display:flex;align-items:center;justify-content:center;white-space:nowrap}
.contact__web{background:var(--dark);color:#fff;flex:1;display:flex;align-items:center;justify-content:center;white-space:nowrap}
</style>
</head>
<body>

<aside class="side-panel side-panel--left">
  <div class="side-panel__brand">Zelqa</div>
  <div class="side-panel__band">
    <span>A</span><span>S</span><span>S</span><span>O</span><span>C</span><span>I</span><span>A</span><span>T</span><span>I</span><span>O</span><span>N</span>
    <span class="side-panel__gap"></span>
    <span>I</span><span>N</span><span>S</span><span>U</span><span>R</span><span>A</span><span>N</span><span>C</span><span>E</span>
  </div>
</aside>

<main class="front">
  <header class="front__header">
    <div class="front__brand">Zelqa</div>
    <svg class="front__divider" width="24" height="62" viewBox="0 0 24 62">
      <line x1="8" y1="2" x2="2" y2="60" stroke="#9fa617" stroke-width="2"/>
      <line x1="15" y1="2" x2="9" y2="60" stroke="#555" stroke-width="1.5"/>
      <line x1="22" y1="2" x2="16" y2="60" stroke="#555" stroke-width="1.5"/>
    </svg>
    <div class="front__tagline">AFFINITY &amp; ASSOCIATION SERVICES</div>
  </header>

  <section class="program">
    <svg width="835" height="214" viewBox="0 0 835 214">
      <rect width="835" height="214" fill="#2f2f2f"/>
      <polygon points="0,0 300,0 380,214 0,214" fill="#9fa617"/>
    </svg>
    <h2 class="program__title">MEMBER<br>INSURANCE<br>PROGRAM<br>MANAGEMENT</h2>
    <ul class="program__list">
      <li style="left:336px;top:32px">Brokerage with A-Rated insurance companies</li>
      <li style="left:348px;top:63px">Full Portfolio of Insurance Products</li>
      <li style="left:358px;top:92px">Full-Service Administrator</li>
      <li style="left:369px;top:120px">State-of-the-Art Technologies</li>
      <li style="left:381px;top:152px">Multi-Channel Marketing</li>
    </ul>
  </section>

  <h2 class="products__title">INSURANCE PRODUCTS</h2>

  <div class="product" style="left:64px;top:460px"><span class="product__icon" role="img" aria-label="Accident icon: figure falling on stairs"></span><span class="product__label">Accident</span></div>
  <div class="product" style="left:165px;top:460px"><span class="product__icon" role="img" aria-label="Business icon: person with umbrella and dollar sign"></span><span class="product__label">Business</span></div>
  <div class="product" style="left:267px;top:460px"><span class="product__icon" role="img" aria-label="Auto icon: car with shield"></span><span class="product__label">Auto</span></div>
  <div class="product" style="left:368px;top:460px"><span class="product__icon" role="img" aria-label="Dental icon: tooth in shield"></span><span class="product__label">Dental</span></div>
  <div class="product" style="left:468px;top:460px"><span class="product__icon" role="img" aria-label="Family health icon: clipboard with medical shield"></span><span class="product__label">Family<br>Health</span></div>
  <div class="product" style="left:570px;top:460px"><span class="product__icon" role="img" aria-label="Financial wellness icon: umbrella over money bag"></span><span class="product__label">Financial<br>Wellness</span></div>
  <div class="product" style="left:671px;top:460px"><span class="product__icon" role="img" aria-label="Long-term care icon: person with walker"></span><span class="product__label">Long-Term<br>Care</span></div>

  <div class="product" style="left:64px;top:599px"><span class="product__icon" role="img" aria-label="Home icon: hands holding a house"></span><span class="product__label">Home</span></div>
  <div class="product" style="left:165px;top:599px"><span class="product__icon" role="img" aria-label="Liability icon: person holding scales"></span><span class="product__label">Liability</span></div>
  <div class="product" style="left:267px;top:599px"><span class="product__icon" role="img" aria-label="Life icon: family group"></span><span class="product__label">Life</span></div>
  <div class="product" style="left:368px;top:599px"><span class="product__icon" role="img" aria-label="Rx cards icon: prescription and pill bottle"></span><span class="product__label">Rx Cards</span></div>
  <div class="product" style="left:468px;top:599px"><span class="product__icon" role="img" aria-label="Travel icon: airplane"></span><span class="product__label">Travel</span></div>
  <div class="product" style="left:570px;top:599px"><span class="product__icon" role="img" aria-label="Vision icon: eye in shield"></span><span class="product__label">Vision</span></div>
  <div class="product" style="left:671px;top:599px"><span class="product__icon" role="img" aria-label="Individual health icon: umbrella over people"></span><span class="product__label">Individual<br>Health</span></div>

  <div class="contact">
    <span class="contact__phone">CALL: 0100 555 0199</span>
    <span class="contact__web">www.zelqagroup.com</span>
  </div>
</main>

<aside class="side-panel side-panel--right">
  <div class="side-panel__brand">Zelqa</div>
  <div class="side-panel__band">
    <span>A</span><span>S</span><span>S</span><span>O</span><span>C</span><span>I</span><span>A</span><span>T</span><span>I</span><span>O</span><span>N</span>
    <span class="side-panel__gap"></span>
    <span>I</span><span>N</span><span>S</span><span>U</span><span>R</span><span>A</span><span>N</span><span>C</span><span>E</span>
  </div>
</aside>

</body>
</html>
```